HomeBridle business card and stationary design

We are looking for a simple yet elegant design for our mortgage company business card and stationary.

The card should include:
Name (Derek Walsh)
Title (CEO)
Phone Number (614-208-3917)
Address (48 Birchfield Court, Suite 314, Marlow, OH 43952)
Email (email@homebridle-example.com)
"NMLS" i.e. (NMLS 61947)
"Company NMLS" (Company NMLS 472815)

See above

```html
<!DOCTYPE html>
<html lang="en">
<head>
<meta charset="utf-8">
<title>HomeBridle Business Card</title>
<link rel="stylesheet" href="https://fonts.googleapis.com/css2?family=Noto+Sans:wght@400;500;600&display=swap">
<style>
  :root {
    --backdrop: #c8bebf;
    --cyan: #4ddcfd;
    --navy: #0e1d2d;
    --pale-teal: #abe1e8;
    --mist: #dfe8e5;
    --mist-light: #e9eeec;
    --sky-soft: #8edfea;
    --icon-teal: #1bb3bf;
    --ring: #8a8f94;
    --white: #ffffff;
  }
  html, body {
    margin: 0;
    padding: 0;
    width: 1200px;
    height: 960px;
    overflow: hidden;
    background: var(--backdrop);
    font-family: "Noto Sans", sans-serif;
  }
  .card {
    position: absolute;
    display: block;
    background: var(--white);
  }
  .card--front { left: 255px; top: 46px; width: 673px; height: 385px; }
  .card--back  { left: 255px; top: 507px; width: 670px; height: 382px; }
  .fill-cyan { fill: var(--cyan); }
  .fill-navy { fill: var(--navy); }
  .fill-teal { fill: var(--pale-teal); }
  .fill-mist { fill: var(--mist); }
  .fill-mist-light { fill: var(--mist-light); }
  .fill-sky { fill: var(--sky-soft); }
  .overlay-band { fill: #c9d6d3; opacity: 0.6; }
  .brand-name {
    font-family: "Noto Sans", sans-serif;
    font-weight: 500;
    fill: var(--navy);
  }
  .person-name { font-weight: 500; font-size: 28px; fill: var(--cyan); letter-spacing: 0.5px; }
  .person-title { font-weight: 400; font-size: 19px; fill: var(--navy); }
  .contact-text { font-weight: 400; font-size: 19px; fill: var(--navy); }
  .company-id { font-weight: 400; font-size: 19px; fill: var(--cyan); }
  .icon-ring { fill: var(--white); stroke: var(--ring); stroke-width: 1.2; }
  .icon-glyph { fill: var(--icon-teal); }
  .icon-at { font-weight: 600; font-size: 20px; fill: var(--icon-teal); }
</style>
</head>
<body>

<svg class="card card--front" viewBox="0 0 841 481" preserveAspectRatio="none" aria-label="Business card front">
  <rect width="841" height="481" fill="#fff"/>
  <rect class="fill-cyan" x="0" y="0" width="841" height="43"/>
  <polygon class="fill-navy" points="538,0 841,0 841,43 567,43"/>
  <polygon class="fill-cyan" points="223,343 841,343 841,481 320,481"/>
  <polygon class="fill-cyan" points="0,442 245,442 272,481 0,481"/>
  <polygon class="overlay-band" points="147,425 681,425 705,481 190,481"/>
  <text class="brand-name" x="421" y="250" font-size="70" text-anchor="middle">HomeBridle</text>
</svg>

<svg class="card card--back" viewBox="0 0 837 478" preserveAspectRatio="none" aria-label="Business card back">
  <rect width="837" height="478" fill="#fff"/>
  <!-- header bands -->
  <polygon class="fill-mist" points="549,0 837,0 837,82 406,82 380,47 580,47"/>
  <polygon class="fill-mist-light" points="724,0 837,0 837,82 755,82 743,47"/>
  <polygon class="fill-sky" points="351,0 549,0 580,47 380,47"/>
  <polygon class="fill-cyan" points="0,0 351,0 380,47 0,47"/>

  <!-- footer bands -->
  <polygon class="fill-mist" points="0,312 367,312 471,460 0,460"/>
  <polygon class="fill-cyan" points="406,368 665,368 708,430 450,430"/>
  <polygon class="fill-teal" points="0,368 407,368 471,460 0,460"/>
  <polygon class="fill-cyan" points="0,460 480,460 492,478 0,478"/>
  <polygon class="fill-navy" points="473,430 837,430 837,478 504,478"/>

  <!-- identity -->
  <text class="person-name" x="51" y="111">DEREK WALSH</text>
  <text class="person-title" x="52" y="142">Chief Executive Officer</text>
  <text class="brand-name" x="780" y="138" font-size="44" text-anchor="end">HomeBridle</text>

  <!-- contact: phone -->
  <circle class="icon-ring" cx="71" cy="282" r="17"/>
  <path class="icon-glyph" d="M64,273 q3,-2 5,1 l2,4 q1,2 -1,3 l-1,1 q2,5 6,7 l1,-1 q1,-2 3,-1 l4,2 q3,2 1,5 q-2,3 -5,2 q-10,-4 -15,-15 q-1,-5 0,-8 z"/>
  <text class="contact-text" x="124" y="289">614-208-3917</text>

  <!-- contact: email -->
  <circle class="icon-ring" cx="71" cy="341" r="17"/>
  <text class="icon-at" x="71" y="348" text-anchor="middle">@</text>
  <text class="contact-text" x="124" y="348">email@homebridle-example.com</text>

  <!-- contact: address -->
  <circle class="icon-ring" cx="71" cy="400" r="17"/>
  <path class="icon-glyph" d="M71,388 a7,7 0 0 1 7,7 q0,5 -7,14 q-7,-9 -7,-14 a7,7 0 0 1 7,-7 z M71,392 a3,3 0 1 0 0.01,0 z" fill-rule="evenodd"/>
  <text class="contact-text" x="125" y="406" font-size="18">48 Birchfield Court, Suite 314, Marlow, OH 43952</text>

  <text class="contact-text" x="125" y="453">NMLS 61947</text>
  <text class="company-id" x="812" y="453" text-anchor="end">Company NMLS 472815</text>
</svg>

</body>
</html>
```